Fruits and Vegetables distribution company needs a new eye catching website

We need to get our website up to date. Our clients will look at our website to learn about our products and services. Our design needs to be simple yet impactful to make our brand memorable to our visitors. We need to have somewhere to tell our clients about our history, products and services, our team. We can throw in a few fun facts and figures and maybe some testimonials to impress. We have 4 theme colors that we want to incorporate into the design, you can get in touch for the HEX/RGB codes. Please remember that smooth operation of any animations and interactions is very important.

Need extra days to review

```html
<!DOCTYPE html>
<html lang="en">
<head>
<meta charset="utf-8">
<title>Orchard Lane — Fruits &amp; Vegetables Distribution</title>
<link href="https://fonts.googleapis.com/css2?family=Jost:wght@400;500;600;700&family=Marcellus&display=swap" rel="stylesheet">
<style>
:root{
  --red:#c5282d;
  --red-dark:#a81e22;
  --yellow:#fbb321;
  --green:#8cc63f;
  --green-pale:#cde6a4;
  --ink:#1a1a1a;
  --text:#444;
  --muted:#8a8a8a;
  --line:#cfcfcf;
  --footer:#161616;
  --white:#fff;
}
*{box-sizing:border-box;margin:0;padding:0}
html,body{width:1200px;height:2970px;overflow:hidden;background:var(--white)}
body{position:relative;font-family:"Jost",Arial,sans-serif;color:var(--text)}
.abs{position:absolute}
.brand{font-family:"Jost",Arial,sans-serif;font-weight:500;letter-spacing:3px;color:var(--red);text-transform:uppercase}

/* header */
.topbar{left:0;top:0;width:1200px;height:107px;background:var(--white)}
.topbar .contact{top:14px;font-size:15px;color:var(--ink);display:flex;align-items:center;gap:12px}
.ico-round{width:30px;height:30px;border-radius:50%;background:var(--yellow);display:flex;align-items:center;justify-content:center}
.social{display:flex;gap:8px}
.social span{width:26px;height:26px;border-radius:50%;border:2px solid var(--yellow);display:block}
.nav{top:66px;font-size:13px;font-weight:600;color:var(--ink);letter-spacing:.3px}
.logo-tab{left:530px;top:0;width:136px;height:134px;background:var(--white);box-shadow:0 4px 10px rgba(0,0,0,.15);display:flex;flex-direction:column;align-items:center;justify-content:center;gap:8px;z-index:3}
.logo-tab .dot{width:36px;height:36px;border-radius:50%;background:var(--yellow)}
.logo-tab .brand{font-size:14px;text-align:center;line-height:1.1}

/* hero */
.hero{left:0;top:107px;width:1200px;height:494px;background:linear-gradient(120deg,#3b6b22 0%,#b8321f 25%,#6a4a2c 45%,#e6b52a 60%,#ddd7cc 75%,#4a2a48 100%)}
.hero-caption{left:0;top:548px;width:1200px;height:53px;background:rgba(0,0,0,.45);color:var(--white);font-weight:600;font-size:29px;text-align:center;line-height:53px;letter-spacing:.5px}
.hero .arrow{top:230px}

/* headings */
.title{font-family:"Marcellus",Georgia,serif;font-size:29px;color:var(--ink);text-align:center;width:1200px;left:0;letter-spacing:.5px}
.rule{height:1px;background:var(--line)}
.lead{left:0;width:1200px;text-align:center;font-size:12px;color:var(--ink)}
.para{left:155px;width:890px;text-align:center;font-size:11.5px;line-height:20px;color:var(--text)}
.btn{background:var(--red);color:var(--white);border-radius:16px;font-size:13px;text-align:center}

/* mission / vision */
.card-mv{top:1060px;height:255px;color:var(--white)}
.card-mv h3{font-family:"Jost",Arial,sans-serif;font-weight:500;font-size:26px;letter-spacing:.5px}
.card-mv p{font-size:12.5px;line-height:20.5px}
.hub{left:505px;top:1093px;width:190px;height:190px;border-radius:50%;background:var(--white);box-shadow:0 0 0 10px #f1f1f1,0 4px 14px rgba(0,0,0,.15);display:flex;flex-direction:column;align-items:center;justify-content:center;gap:8px;z-index:2}
.badge{width:114px;height:114px;border-radius:50%;border:6px solid var(--white);box-shadow:0 2px 8px rgba(0,0,0,.2);display:flex;align-items:center;justify-content:center;z-index:2}

/* products */
.products{left:0;top:1395px;width:1200px;height:612px;background:var(--green-pale)}
.prod{top:1595px;width:282px;height:332px;background:var(--white);box-shadow:0 2px 8px rgba(0,0,0,.15);border-bottom:3px solid var(--red-dark)}
.prod .photo{position:absolute;left:6px;top:6px;width:270px;height:182px}
.prod h4{position:absolute;top:206px;width:100%;text-align:center;font-size:19px;font-weight:500;color:var(--ink)}
.prod p{position:absolute;left:22px;top:240px;width:238px;text-align:center;font-size:11.5px;line-height:20px}
.prod .plus{position:absolute;left:120px;top:310px;width:42px;height:21px;border-radius:21px 21px 0 0;background:var(--red);color:var(--white);text-align:center;font-size:18px;line-height:24px;font-weight:600}

/* testimonial */
.quote{left:310px;top:2180px;width:580px;height:215px;background:var(--white);border-radius:6px;box-shadow:0 2px 12px rgba(0,0,0,.12)}
.quote p{position:absolute;left:55px;top:28px;width:470px;text-align:center;font-size:12.5px;line-height:22px;color:var(--ink)}
.quote .name{position:absolute;top:168px;width:100%;text-align:center;color:var(--yellow);font-size:14px;font-weight:600}
.qmark{font-family:"Marcellus",Georgia,serif;font-size:70px;color:#ddd;line-height:1}

/* footer */
.footer{left:0;top:2500px;width:1200px;height:425px;background:var(--footer)}
.f-head{font-size:24px;font-weight:500;color:var(--white);letter-spacing:.5px}
.f-row{display:flex;gap:14px;font-size:12px;color:#ddd;line-height:16px}
.form{left:422px;top:2490px;width:355px;height:396px;background:var(--green);border-radius:6px 6px 0 0}
.field{position:absolute;left:30px;width:295px;height:30px;background:var(--white);font-size:11px;color:#555;padding:7px 8px}
.legal{left:0;top:2925px;width:1200px;height:45px;background:var(--red);color:var(--white);font-size:12px;text-align:center;line-height:45px}
</style>
</head>
<body>

<!-- header -->
<header class="abs topbar">
  <div class="abs contact" style="left:140px">
    <span class="ico-round"><svg width="14" height="10" viewBox="0 0 14 10"><rect x="0.5" y="0.5" width="13" height="9" fill="none" stroke="#fff"/><path d="M0.5 0.5 7 6 13.5 0.5" fill="none" stroke="#fff"/></svg></span>
    info@orchardlane.com
  </div>
  <div class="abs contact" style="left:745px">
    <span class="ico-round"><svg width="14" height="14" viewBox="0 0 24 24"><path d="M6.6 10.8a15 15 0 0 0 6.6 6.6l2.2-2.2c.3-.3.7-.4 1-.2 1.1.4 2.3.6 3.6.6.6 0 1 .4 1 1V20c0 .6-.4 1-1 1A17 17 0 0 1 3 4c0-.6.4-1 1-1h3.5c.6 0 1 .4 1 1 0 1.3.2 2.5.6 3.6.1.3 0 .7-.2 1z" fill="#fff"/></svg></span>
    <span style="font-size:17px;letter-spacing:1px">123-555-0190</span>
    <span class="social" style="margin-left:16px"><span></span><span></span><span></span><span></span></span>
  </div>
  <svg class="abs" style="left:138px;top:66px" width="18" height="16" viewBox="0 0 18 16"><path d="M9 1 1 8h2.5v7h4.5v-5h2v5h4.5V8H17z" fill="#8cc63f"/></svg>
  <nav>
    <span class="abs nav" style="left:188px">OUR HISTORY</span>
    <span class="abs nav" style="left:320px">DIVISIONS</span>
    <span class="abs nav" style="left:438px">PRODUCT</span>
    <span class="abs nav" style="left:695px">SERVICES</span>
    <span class="abs nav" style="left:815px">MEDIA COVERAGE</span>
    <span class="abs nav" style="left:993px">CONTACT</span>
  </nav>
  <div class="abs logo-tab"><span class="dot"></span><span class="brand">Orchard<br>Lane</span></div>
</header>

<!-- hero -->
<section class="abs hero" role="img" aria-label="Fresh tomatoes, cucumbers, yellow peppers in a basket, garlic, greens and aubergines on a wooden table">
  <svg class="abs arrow" style="left:50px" width="24" height="44" viewBox="0 0 24 44"><path d="M20 2 4 22l16 20" fill="none" stroke="rgba(255,255,255,.7)" stroke-width="3"/></svg>
  <svg class="abs arrow" style="left:1118px" width="24" height="44" viewBox="0 0 24 44"><path d="M4 2l16 20L4 42" fill="none" stroke="rgba(255,255,255,.7)" stroke-width="3"/></svg>
</section>
<div class="abs hero-caption">WE ARE A FRUITS &amp; VEGETABLES DISTRIBUTION COMPANY</div>

<!-- welcome -->
<div class="abs rule" style="left:428px;top:681px;width:80px"></div>
<div class="abs rule" style="left:695px;top:681px;width:80px"></div>
<h1 class="abs title" style="top:662px">WELCOME TO</h1>
<div class="abs" style="left:0;top:715px;width:1200px;display:flex;flex-direction:column;align-items:center;gap:6px">
  <span style="width:34px;height:34px;border-radius:50%;background:var(--yellow)"></span>
  <span class="brand" style="font-size:17px">Orchard Lane</span>
</div>
<p class="abs lead" style="top:832px">Lorem ipsum dolor sit amet, consectetuer adipiscing elit, sed diam nonummy nibh euismod tincidunt ut laoreet</p>
<p class="abs para" style="top:868px">Lorem ipsum dolor sit amet, consectetuer adipiscing elit, sed diam nonummy nibh euismod tincidunt ut laoreet dolore magna aliquam erat volutpat. Ut wisi enim ad minim veniam, quis nostrud exerci tation ullamcorper suscipit lobortis nisl ut aliquip ex ea commodo consequat. Duis autem vel eum iriure dolor in hendrerit in vulputate velit esse molestie consequat, vel illum dolore eu feugiat nulla facilisis at vero eros et accumsan et iusto odio dignissim qui blandit praesent luptatum zzril delenit</p>
<div class="abs btn" style="left:546px;top:969px;width:108px;height:32px;line-height:32px">Read More</div>

<!-- mission / vision -->
<svg class="abs" style="left:140px;top:1060px" width="415" height="255" viewBox="0 0 415 255"><path d="M10 0H380l35 40v175l-35 40H10A10 10 0 0 1 0 245V10A10 10 0 0 1 10 0z" fill="#fbb321"/></svg>
<div class="abs card-mv" style="left:215px;width:270px">
  <h3 style="margin-top:38px">OUR MISSION</h3>
  <p style="margin-top:10px">Lorem ipsum dolor sit amet, consect etuer adipi scing elit, sed diam nonummy nibh euismod tincidunt ut laoreet dolore magna aliquam erat volutpat. Ut wisi enim ad minim veniam, quis nostrud exerci tation ullamc orper suscipit lobortis nisl ut aliquip ex ea commodo consequat.</p>
</div>
<svg class="abs" style="left:650px;top:1060px" width="410" height="255" viewBox="0 0 410 255"><path d="M35 0H400a10 10 0 0 1 10 10v235a10 10 0 0 1-10 10H35L0 215V40z" fill="#c5282d"/></svg>
<div class="abs card-mv" style="left:718px;width:270px">
  <h3 style="margin-top:26px;text-align:right">OUR VISION</h3>
  <p style="margin-top:8px">Lorem ipsum dolor sit amet, consect etuer adipi scing elit, sed diam nonummy nibh euismod tincidunt ut laoreet dolore magna aliquam erat volutpat. Ut wisi enim ad minim veniam, quis nostrud exerci tation ullamc orper suscipit lobortis nisl ut aliquip ex ea commodo consequat.</p>
</div>
<div class="abs badge" style="left:84px;top:1130px;background:var(--red)">
  <svg width="56" height="56" viewBox="0 0 56 56"><circle cx="28" cy="28" r="24" fill="none" stroke="#fff" stroke-width="4"/><circle cx="28" cy="28" r="15" fill="none" stroke="#fff" stroke-width="4"/><circle cx="28" cy="28" r="6" fill="#fff"/><path d="M28 28 50 6" stroke="#fff" stroke-width="3"/></svg>
</div>
<div class="abs badge" style="left:1000px;top:1127px;background:var(--yellow)">
  <svg width="56" height="40" viewBox="0 0 56 40"><path d="M2 20C10 8 18 3 28 3s18 5 26 17c-8 12-16 17-26 17S10 32 2 20z" fill="#fff"/><circle cx="28" cy="20" r="10" fill="#fbb321"/><circle cx="28" cy="20" r="5" fill="#fff"/></svg>
</div>
<div class="abs hub"><span style="width:38px;height:38px;border-radius:50%;background:var(--yellow)"></span><span class="brand" style="font-size:17px;text-align:center;line-height:1.1">Orchard<br>Lane</span></div>

<!-- products -->
<section class="abs products"></section>
<h2 class="abs title" style="top:1467px">PRODUCTS AND SERVICES</h2>
<div class="abs rule" style="left:455px;top:1526px;width:120px;background:#777"></div>
<div class="abs rule" style="left:625px;top:1526px;width:120px;background:#777"></div>
<svg class="abs" style="left:588px;top:1512px" width="24" height="26" viewBox="0 0 24 26"><circle cx="12" cy="15" r="9" fill="none" stroke="#444" stroke-width="1.5"/><path d="M12 6V2" stroke="#444" stroke-width="1.5"/></svg>
<p class="abs lead" style="top:1552px;font-size:11.5px;color:var(--text)">Duis autem vel eum iriure dolor in hendrerit inknl vulputate velit esse molestie consequat, vel illum dolore eumar feugiat nulla facilisis.</p>

<article class="abs prod" style="left:150px">
  <div class="photo" role="img" aria-label="Basket of assorted fresh fruit" style="background:linear-gradient(135deg,#d9472b,#e9a23b 50%,#6f8a2d)"></div>
  <h4>Fresh Fruit</h4>
  <p>Lorem ipsum dolor sit amet, consectetuerpiscing elit, sed diam nonummy nibh euismod tincidunt ut laoreet dolore magna aliquam erat</p>
  <span class="plus">+</span>
</article>
<article class="abs prod" style="left:460px">
  <div class="photo" role="img" aria-label="Colourful assortment of fresh vegetables" style="background:linear-gradient(135deg,#e7772a,#c6282b 45%,#4f8f2a)"></div>
  <h4>Fresh Vegetables</h4>
  <p>Lorem ipsum dolor sit amet, consectetuerpiscing elit, sed diam nonummy nibh euismod tincidunt ut laoreet dolore magna aliquam erat</p>
  <span class="plus">+</span>
</article>
<article class="abs prod" style="left:772px">
  <div class="photo" role="img" aria-label="Milk jug, cheeses and grains on a wooden table" style="background:linear-gradient(135deg,#3a2c22,#8a6a4a 55%,#e8dcc0)"></div>
  <h4>Other Products</h4>
  <p>Lorem ipsum dolor sit amet, consectetuerpiscing elit, sed diam nonummy nibh euismod tincidunt ut laoreet dolore magna aliquam erat</p>
  <span class="plus">+</span>
</article>

<!-- testimonials -->
<h2 class="abs title" style="top:2078px">CLIENT TESTIMONIALS</h2>
<div class="abs rule" style="left:455px;top:2136px;width:120px;background:#777"></div>
<div class="abs rule" style="left:625px;top:2136px;width:120px;background:#777"></div>
<svg class="abs" style="left:588px;top:2122px" width="24" height="26" viewBox="0 0 24 26"><circle cx="12" cy="15" r="9" fill="none" stroke="#444" stroke-width="1.5"/><path d="M12 6V2" stroke="#444" stroke-width="1.5"/></svg>
<div class="abs" role="img" aria-label="Smiling customer holding a paper bag of fresh groceries" style="left:140px;top:2112px;width:175px;height:388px;background:linear-gradient(180deg,#e9e3dc,#b89a78 45%,#8fa9c4);border-radius:80px 80px 0 0"></div>
<div class="abs quote">
  <span class="abs qmark" style="left:14px;top:8px">&ldquo;</span>
  <p>Lorem ipsum dolor sit amet, consectetuer adipiscing elit, sed diam nonummy nibhismod tincidunt ut laoreet dolore magna aliquam erat volutpat. Ut wisi enim ad minimveniam, quis nostrud exerci tation ullamcorper suscipit lobortis nisl ut aliquip ex ea commodo consequat. Duis autem vel eum iriure dolor in hendrerit in vulputate velit esse molestie consequat, quis nostrud exerci tation ullamcorper</p>
  <span class="abs qmark" style="left:440px;top:98px">&rdquo;</span>
  <span class="name">- Ms. Clara Mendes</span>
</div>
<div class="abs" style="left:875px;top:2270px;width:30px;height:30px;border-radius:50%;background:var(--white);box-shadow:0 1px 5px rgba(0,0,0,.2);text-align:center;line-height:28px;font-size:16px;color:var(--ink)">&raquo;</div>

<!-- footer -->
<footer class="abs footer">
  <h3 class="abs f-head" style="left:142px;top:42px">CONTACT DETAILS</h3>
  <div class="abs rule" style="left:142px;top:88px;width:218px;background:#444"></div>
  <div class="abs f-row" style="left:142px;top:112px">
    <svg width="16" height="20" viewBox="0 0 16 20"><path d="M8 0a7 7 0 0 0-7 7c0 5 7 13 7 13s7-8 7-13a7 7 0 0 0-7-7z" fill="#8cc63f"/><circle cx="8" cy="7" r="2.5" fill="#161616"/></svg>
    <div><b style="color:#fff;font-weight:600;letter-spacing:1px">ORCHARD LANE</b><br>123 euismod cidun ut laoreetmok<br>laoreet dol magnak aliquam</div>
  </div>
  <div class="abs f-row" style="left:142px;top:200px"><svg width="16" height="16" viewBox="0 0 24 24"><path d="M6.6 10.8a15 15 0 0 0 6.6 6.6l2.2-2.2c.3-.3.7-.4 1-.2 1.1.4 2.3.6 3.6.6.6 0 1 .4 1 1V20c0 .6-.4 1-1 1A17 17 0 0 1 3 4c0-.6.4-1 1-1h3.5c.6 0 1 .4 1 1 0 1.3.2 2.5.6 3.6.1.3 0 .7-.2 1z" fill="#8cc63f"/></svg>123 555 0190</div>
  <div class="abs f-row" style="left:142px;top:244px"><svg width="16" height="12" viewBox="0 0 16 12"><rect width="16" height="12" fill="#8cc63f"/><path d="M0 0 8 7 16 0" fill="none" stroke="#161616" stroke-width="1.5"/></svg>info@orchardlane.com</div>
  <h3 class="abs f-head" style="left:142px;top:300px;font-size:18px">FOLLOW US</h3>
  <div class="abs rule" style="left:142px;top:332px;width:218px;background:#444"></div>
  <div class="abs" style="left:150px;top:354px;display:flex;gap:20px"><span style="width:14px;height:14px;border-radius:50%;background:#fff"></span><span style="width:14px;height:14px;border-radius:50%;background:#fff"></span><span style="width:14px;height:14px;border-radius:50%;background:#fff"></span><span style="width:14px;height:14px;border-radius:50%;background:#fff"></span></div>
  <div class="abs" style="left:820px;top:100px;width:240px;display:flex;flex-direction:column;align-items:center;gap:18px">
    <span style="width:90px;height:90px;border-radius:50%;background:var(--yellow)"></span>
    <span class="brand" style="font-size:34px;color:#fff;letter-spacing:4px;text-align:center;line-height:1.1">Orchard<br>Lane</span>
  </div>
</footer>
<section class="abs form">
  <h3 class="abs f-head" style="left:30px;top:42px">GET IN TOUCH</h3>
  <div class="abs rule" style="left:30px;top:90px;width:295px;background:rgba(255,255,255,.5)"></div>
  <div class="field" style="top:122px">Name</div>
  <div class="field" style="top:163px">Email</div>
  <div class="field" style="top:204px">Phone</div>
  <div class="field" style="top:245px;height:68px">Message</div>
  <div class="abs" style="left:30px;top:326px;width:295px;height:30px;border:2px solid #fff;color:#fff;font-size:13px;text-align:center;line-height:26px">SUBMIT</div>
</section>
<div class="abs legal">Copyright © 2018 &nbsp;<span style="letter-spacing:2px;font-weight:500">ORCHARD LANE</span>&nbsp; All Right Reserved.</div>

</body>
</html>
```